Brand Identity Stationary Package

Hello I'm looking for a full branding package for my Property Management Company. I have a logo but looking to have the following
Business Card
Email signature
Facebook cover photo
Letterhead (word.doc)
#10 Envelope
Pocket Folder - link to 9x12 pocket folder design specs https://www.quillpress.ca/marketing-materials/presentation-folders
would like everything to match and be brand identifiable. The company looks after residential properties/apartments and some commercial properties. Attached is a zip of the files.
For Business Card
Name: Morgan Tillsey
Position: Operations Manager
Number: 1 (506) 384-2971
Email: Morgan@harbrook.ca
Website: Harbrook.ca
Industry/Entity Type
Property Management

```html
<!DOCTYPE html>
<html lang="en">
<head>
<meta charset="utf-8">
<title>Harbrook Stationery Set</title>
<link rel="stylesheet" href="https://fonts.googleapis.com/css2?family=Roboto:wght@400;500;700&display=swap">
<style>
  :root {
    --bg: #e9e9e9;
    --paper: #f7f7f7;
    --ink: #1f1f1f;
    --text: #555555;
    --green: #7aa946;
    --white: #f2f2f2;
    --photo-top: #2e3132;
    --photo-bottom: #6f7475;
  }
  * { margin: 0; padding: 0; box-sizing: border-box; }
  html, body { width: 1200px; height: 795px; overflow: hidden; }
  body {
    position: relative;
    background: var(--bg);
    font-family: "Roboto", Arial, sans-serif;
    color: var(--text);
  }
  .sheet { position: absolute; background: var(--paper); overflow: hidden; }
  .brand-name {
    position: absolute;
    font-family: "Roboto", Arial, sans-serif;
    font-weight: 700;
    letter-spacing: 0.08em;
    white-space: nowrap;
    line-height: 1;
  }
  .brand-dark { color: var(--ink); }
  .brand-light { color: var(--white); }
  .band { position: absolute; left: 0; right: 0; bottom: 0; }
  .band svg { display: block; width: 100%; height: 100%; }
  .icon { display: inline-block; width: 4px; height: 4px; background: var(--green); border-radius: 1px; margin-right: 2px; vertical-align: -0.3px; }

  /* Letterhead */
  .letterhead { left: 292px; top: 99px; width: 293px; height: 414px; }
  .letterhead .brand-name { left: 31px; top: 35px; font-size: 14px; }
  .letterhead .contact { position: absolute; left: 196px; top: 27px; font-size: 5.2px; line-height: 7px; }
  .letter-body { position: absolute; left: 32px; top: 106px; width: 231px; font-size: 5.3px; line-height: 7.6px; }
  .letter-body p { margin-bottom: 7.6px; text-align: justify; }
  .signature { position: absolute; left: 32px; top: 306px; width: 34px; height: 30px; background: linear-gradient(135deg, #e6e6e6, #d9d9d9); border-radius: 2px; }
  .letterhead .band { height: 7px; }

  /* Folder */
  .folder { left: 637px; top: 80px; width: 346px; height: 437px; background: var(--ink); }
  .folder .brand-name { left: 0; right: 0; top: 104px; text-align: center; font-size: 27px; }
  .folder-photo {
    position: absolute; left: 0; right: 0; top: 217px; bottom: 0;
    background: linear-gradient(180deg, var(--photo-top), var(--photo-bottom));
  }

  /* Business cards */
  .card-front { left: 186px; top: 550px; width: 133px; height: 75px; background: var(--ink); }
  .card-front .brand-name { left: 0; right: 0; top: 29px; text-align: center; font-size: 13px; }
  .card-front .url { position: absolute; left: 0; right: 0; top: 60px; text-align: center; font-size: 4.3px; color: var(--white); letter-spacing: 0.05em; }
  .card-front .url b { color: var(--green); font-weight: 400; }

  .card-back { left: 186px; top: 646px; width: 133px; height: 75px; }
  .card-back .brand-name { right: 11px; top: 15px; font-size: 7.5px; }
  .card-back .person { position: absolute; left: 11px; top: 39px; font-size: 4.2px; line-height: 4.6px; color: var(--ink); }
  .card-back .person .name { font-weight: 500; text-transform: uppercase; }
  .card-back .person .name b { color: var(--green); font-weight: 500; }
  .card-back .rule { position: absolute; left: 50px; right: 11px; top: 45px; height: 0.5px; background: #999; }
  .card-back .details { position: absolute; left: 11px; top: 51px; font-size: 3.6px; line-height: 4.6px; color: var(--ink); }
  .card-back .details .icon { width: 3px; height: 3px; margin-right: 1.5px; }
  .card-back .address { position: absolute; right: 11px; top: 55px; font-size: 3.6px; line-height: 4.4px; color: var(--ink); text-align: right; }
  .card-back .band { height: 4px; }

  /* Envelope front */
  .envelope-front { left: 353px; top: 563px; width: 329px; height: 155px; }
  .envelope-front .brand-name { left: 21px; top: 22px; font-size: 13px; }
  .envelope-front .return-address { position: absolute; left: 21px; top: 41px; width: 96px; text-align: center; font-size: 6.4px; line-height: 7.6px; color: #444; }
  .envelope-front .band { height: 8px; }

  /* Envelope back */
  .envelope-back { left: 714px; top: 561px; width: 328px; height: 157px; }
  .envelope-back .flap { position: absolute; left: 0; top: 0; width: 328px; height: 56px; }
  .envelope-back .brand-name { left: 0; right: 0; top: 20px; text-align: center; font-size: 12px; }
</style>
</head>
<body>

  <!-- Letterhead -->
  <section class="sheet letterhead">
    <div class="brand-name brand-dark">HARBROOK</div>
    <div class="contact">
      48 Larchmont Crescent,<br>
      Aurora, ON L4G 3K7<br>
      <span class="icon"></span>1 (506) 384-2971<br>
      <span class="icon"></span>Morgan@harbrook.ca<br>
      <span class="icon"></span>www.harbrook.ca
    </div>
    <div class="letter-body">
      <p>Dear customer,</p>
      <p>Lorem ipsum dolor sit amet, consectetur adipisicing elit, sed do eiusmod tempor incididunt ut labore et dolore magna aliqua. Ut enim ad minim veniam, quis nostrud exercitation ullamco laboris nisi ut aliquip ex ea commodo consequat. Duis aute irure dolor in reprehenderit in voluptate velit esse cillum dolore eu fugiat nulla pariatur. Excepteur sint occaecat cupidatat non proident, sunt in culpa qui officia deserunt mollit anim id est laborum.</p>
      <p>Lorem ipsum dolor sit amet, consectetur adipisicing elit, sed do eiusmod tempor incididunt ut labore et dolore magna aliqua. Ut enim ad minim veniam, quis nostrud exercitation ullamco laboris nisi ut aliquip ex ea commodo consequat. Duis aute irure dolor in reprehenderit in voluptate velit esse cillum dolore eu fugiat nulla pariatur. Excepteur sint occaecat cupidatat non proident, sunt in culpa qui officia deserunt mollit anim id est laborum.</p>
      <p>Lorem ipsum dolor sit amet, consectetur adipisicing elit, sed do eiusmod tempor incididunt ut labore et dolore magna aliqua. Ut enim ad minim veniam, quis nostrud exercitation ullamco laboris nisi ut aliquip ex ea commodo consequat. Duis aute irure dolor in reprehenderit in voluptate velit esse cillum dolore eu fugiat nulla pariatur. Excepteur sint occaecat cupidatat non proident, sunt in culpa qui officia deserunt mollit anim id est laborum.</p>
      <p>Lorem ipsum dolor sit amet, consectetur adipisicing elit, sed do eiusmod tempor incididunt ut labore et dolore magna aliqua. Ut enim ad minim veniam, quis nostrud exercitation ullamco laboris nisi ut aliquip ex ea commodo consequat. Duis aute irure dolor in reprehenderit.</p>
      <p>Yours Sincerely,</p>
    </div>
    <div class="signature" role="img" aria-label="Handwritten signature"></div>
    <div class="band">
      <svg viewBox="0 0 293 7" preserveAspectRatio="none">
        <rect width="293" height="7" fill="var(--green)"/>
        <polygon points="0,0 59,0 53,7 0,7" fill="var(--ink)"/>
        <polygon points="59,0 61,0 55,7 53,7" fill="var(--paper)"/>
      </svg>
    </div>
  </section>

  <!-- Pocket folder -->
  <section class="sheet folder">
    <div class="brand-name brand-light">HARBROOK</div>
    <div class="folder-photo" role="img" aria-label="Architectural photograph of a modern building"></div>
  </section>

  <!-- Business card, front -->
  <section class="sheet card-front">
    <div class="brand-name brand-light">HARBROOK</div>
    <div class="url">www.<b>harbrook</b>.ca</div>
  </section>

  <!-- Business card, back -->
  <section class="sheet card-back">
    <div class="brand-name brand-dark">HARBROOK</div>
    <div class="person">
      <div class="name">Morgan <b>Tillsey</b></div>
      <div>Operations Manager</div>
    </div>
    <div class="rule"></div>
    <div class="details">
      <span class="icon"></span>1 (506) 384-2971<br>
      <span class="icon"></span>Morgan@harbrook.ca<br>
      <span class="icon"></span>www.harbrook.ca
    </div>
    <div class="address">
      62 Fenwick Road<br>Kingsford 4021
    </div>
    <div class="band">
      <svg viewBox="0 0 133 4" preserveAspectRatio="none">
        <rect width="133" height="4" fill="var(--green)"/>
        <polygon points="0,0 21,0 19,4 0,4" fill="var(--ink)"/>
      </svg>
    </div>
  </section>

  <!-- Envelope, front -->
  <section class="sheet envelope-front">
    <div class="brand-name brand-dark">HARBROOK</div>
    <div class="return-address">Unit 2 / 17 Quayside Lane,<br>Meadowbank, NSW 2114</div>
    <div class="band">
      <svg viewBox="0 0 329 8" preserveAspectRatio="none">
        <rect width="329" height="8" fill="var(--green)"/>
        <polygon points="0,0 67,0 60,8 0,8" fill="var(--ink)"/>
        <polygon points="67,0 69,0 62,8 60,8" fill="var(--paper)"/>
      </svg>
    </div>
  </section>

  <!-- Envelope, back -->
  <section class="sheet envelope-back">
    <svg class="flap" viewBox="0 0 328 56" preserveAspectRatio="none">
      <path d="M0,0 H328 L322,48 Q321,55 314,55 H14 Q7,55 6,48 Z" fill="var(--ink)"/>
    </svg>
    <div class="brand-name brand-light">HARBROOK</div>
  </section>

</body>
</html>
```